Create a Flyer for a Darts Tournament

We need a Flyer for a Darts Tournament that is going to be organized by our darts department (logo attached). The name of the tournament is "3. KLW Dartsturnier". The Flyer should look modern, professional and in a way that everyone can see at the first impression that is has to do with dart sports. The logo of our department should be on the flyer as well. On the flyer we need an area where we can place some informations regarding the tournament (bullet points) etc. And a area where we can place informations regarding the registration progress (e.g. "Registration via E-Mail". Should fit well to our logo.

Target Market(s)

Darts Players for the Tournament

Font styles to use
Serif

Colors

Designer to choose colors to be used in the design.

Requirements
Must have
• Name of the Tournament, our Logo, place for some tournament details, link to our registration page (besucher.tv-hallwitz.de). Should

```html
<!DOCTYPE html>
<html lang="de">
<head>
<meta charset="utf-8">
<title>3. KLW Dartsturnier</title>
<link rel="stylesheet" href="https://fonts.googleapis.com/css2?family=Bebas+Neue&family=Orbitron:wght@800;900&family=Oswald:wght@200;300&family=Poppins:wght@300;400;500;600;700&display=swap">
<style>
:root{
  --ink:#161718;
  --row:#262728;
  --cyan:#12c6f2;
  --cyan-bright:#1de4ff;
  --blue:#1366a8;
  --blue-deep:#0c3d66;
  --white:#ffffff;
  --grey:#cfd3d6;
}
*{margin:0;padding:0;box-sizing:border-box}
html,body{width:946px;height:1200px;overflow:hidden;background:var(--ink)}
.flyer{position:relative;width:946px;height:1200px;overflow:hidden;
  background:linear-gradient(180deg,#10324f 0%,#142638 14%,#18191a 34%,#1b1c1d 100%);
  font-family:"Poppins",sans-serif;color:var(--white)}
.stage-lights{position:absolute;left:0;top:0;width:946px;height:260px;
  background:
   radial-gradient(ellipse 180px 70px at 90px 20px,rgba(170,240,255,.75),transparent 70%),
   radial-gradient(ellipse 180px 70px at 856px 20px,rgba(170,240,255,.75),transparent 70%),
   radial-gradient(ellipse 520px 240px at 473px 0,rgba(25,130,200,.45),transparent 75%)}
.title-number{position:absolute;left:473px;top:64px;transform:translateX(-50%);white-space:nowrap;
  font-family:"Orbitron",sans-serif;font-weight:900;font-size:168px;line-height:1;letter-spacing:-4px;
  background:linear-gradient(90deg,var(--cyan-bright),#10c0f5 60%,#1ad0ff);
  -webkit-background-clip:text;background-clip:text;color:transparent}
.title-word{position:absolute;left:475px;top:222px;white-space:nowrap;
  font-family:"Bebas Neue",sans-serif;font-weight:400;font-size:182px;line-height:1;
  transform:translateX(-50%) scaleX(.88);transform-origin:center}
.times{position:absolute;left:40px;top:386px;width:543px;height:122px;
  background:linear-gradient(90deg,transparent 0%,rgba(19,102,168,.55) 25%,var(--blue) 100%)}
.time-line{position:absolute;left:68px;font-size:30px;font-weight:300;color:var(--cyan);white-space:nowrap;letter-spacing:-.5px}
.time-line b{font-weight:600;color:var(--white)}
.time-line.entry{top:12px}
.time-line.start{top:68px}
.times .divider{position:absolute;left:70px;right:20px;top:62px;border-top:1px dashed rgba(255,255,255,.45)}
.day{position:absolute;left:598px;top:380px;width:240px;text-align:right;
  font-family:"Bebas Neue",sans-serif;font-size:82px;line-height:1;color:var(--cyan)}
.date{position:absolute;left:598px;top:446px;width:240px;text-align:right;
  font-family:"Oswald",sans-serif;font-weight:200;font-size:64px;line-height:1;letter-spacing:-3px}
.club-name{position:absolute;left:108px;top:594px;width:164px;display:flex;align-items:center;gap:10px;
  font-size:26px;font-weight:700;line-height:1.05}
.club-name .dot{width:18px;height:18px;border-radius:50%;background:var(--cyan);flex:none}
.format{position:absolute;left:300px;top:544px;font-size:19.5px;line-height:1.25}
.format strong{font-weight:700}
.format span{font-weight:500}
.venue{position:absolute;left:300px;top:590px;width:380px;height:44px;display:flex;align-items:center;gap:14px;
  background:linear-gradient(90deg,#10395d 0%,#173349 60%,transparent 100%)}
.venue svg{flex:none;margin-left:2px}
.venue p{font-size:15px;letter-spacing:2.6px;line-height:1.03;font-weight:400}
.capacity{position:absolute;left:690px;top:550px;width:158px;height:131px;border:2px solid var(--cyan);border-radius:6px;
  text-align:center;padding-top:7px}
.capacity .label{font-size:19px;font-weight:600;letter-spacing:.5px}
.capacity .count{font-family:"Orbitron",sans-serif;font-weight:900;font-size:56px;line-height:.95;color:var(--cyan)}
.capacity .unit{font-size:16px;font-weight:600;letter-spacing:.2px;margin-top:6px}
.details{position:absolute;left:0;top:725px;width:946px;list-style:none}
.details li{position:relative;height:45px;margin-bottom:19px;padding:7px 14px 0 548px;
  background:linear-gradient(90deg,rgba(40,41,42,.6),var(--row) 60%,rgba(30,31,32,.8));
  font-size:11.6px;line-height:1.3;color:var(--grey);white-space:nowrap}
.details li svg{position:absolute;left:524px;top:10px}
.details li strong{color:var(--cyan);font-weight:600}
.board-photo{position:absolute;left:0;top:695px;width:515px;height:505px;
  border-top-right-radius:260px;
  background:radial-gradient(ellipse 300px 300px at 200px 260px,#5c5f60 0%,#3a3b3c 45%,#232425 75%,#1b1c1d 100%)}
.rules{position:absolute;left:531px;top:1001px;width:361px}
.rule{display:flex;height:30px;margin-bottom:6px;border-radius:15px;overflow:hidden;font-size:16px}
.rule .phase{width:157px;background:var(--cyan);color:#0b2233;padding-left:16px;line-height:30px;font-weight:400}
.rule .mode{flex:1;background:var(--blue-deep);font-family:"Orbitron",sans-serif;font-weight:800;font-size:15px;line-height:30px;text-align:center;letter-spacing:.5px}
.signup{position:absolute;left:515px;top:1081px;width:431px;height:54px;background:#111213;
  display:flex;align-items:center;padding-left:16px;gap:10px}
.signup .label{font-family:"Bebas Neue",sans-serif;font-size:18px;color:var(--cyan);transform:scaleX(.85);transform-origin:left;white-space:nowrap;margin-right:-14px}
.signup .bar{width:1px;height:20px;background:var(--cyan)}
.signup .link{font-size:16.5px;font-weight:400}
.website{position:absolute;left:531px;top:1151px;font-size:15px;letter-spacing:4.6px;font-weight:300}
.website b{font-weight:700}
</style>
</head>
<body>
<main class="flyer">
  <div class="stage-lights" role="img" aria-label="Stadionscheinwerfer im Hintergrund"></div>

  <h1>
    <span class="title-number">3.KLW</span>
    <span class="title-word">DARTSTURNIER</span>
  </h1>

  <div class="times">
    <p class="time-line entry">EINLASS <b>16:00 UHR</b></p>
    <div class="divider"></div>
    <p class="time-line start">TURNIERBEGINN <b>17:00 UHR</b></p>
  </div>
  <p class="day">SAMSTAG</p>
  <p class="date">25.01.2025</p>

  <div class="club-name"><span class="dot"></span><span>KLW<br>DARTS</span></div>

  <p class="format"><strong>Steel-Darts-Hobbyturnier</strong><br><span>(keine Ligaspieler)</span></p>

  <div class="venue">
    <svg width="26" height="36" viewBox="0 0 26 36" aria-hidden="true"><path d="M13 1C6.4 1 1 6.2 1 12.8 1 21 13 35 13 35s12-14 12-22.2C25 6.2 19.6 1 13 1z" fill="#12c6f2"/><circle cx="13" cy="12.5" r="4.8" fill="#161718"/></svg>
    <p>SVZ IN 54321<br>HALLWITZ-AUE</p>
  </div>

  <div class="capacity">
    <p class="label">MAXIMAL</p>
    <p class="count">48</p>
    <p class="unit">TEILNEHMER</p>
  </div>

  <ul class="details">
    <li><svg width="12" height="12" viewBox="0 0 12 12" aria-hidden="true"><circle cx="6" cy="6" r="6" fill="#12c6f2"/><path d="M3.2 6.2l2 2 3.6-4" stroke="#1b1c1d" stroke-width="1.5" fill="none"/></svg><strong>Eröffnungszeremonie:</strong> Auftakt mit Vorstellung der<br>Spieler und Bekanntgabe der Turnierregeln.</li>
    <li><svg width="12" height="12" viewBox="0 0 12 12" aria-hidden="true"><circle cx="6" cy="6" r="6" fill="#12c6f2"/><path d="M3.2 6.2l2 2 3.6-4" stroke="#1b1c1d" stroke-width="1.5" fill="none"/></svg><strong>Herausforderung für höchste Punktzahl:</strong> Preis für<br>die höchste Einzelpunktzahl.</li>
    <li><svg width="12" height="12" viewBox="0 0 12 12" aria-hidden="true"><circle cx="6" cy="6" r="6" fill="#12c6f2"/><path d="M3.2 6.2l2 2 3.6-4" stroke="#1b1c1d" stroke-width="1.5" fill="none"/></svg><strong>Doppel-K.O.-Runden:</strong> Die Teams treten in spannenden<br>Ausscheidungsrunden gegeneinander an.</li>
    <li><svg width="12" height="12" viewBox="0 0 12 12" aria-hidden="true"><circle cx="6" cy="6" r="6" fill="#12c6f2"/><path d="M3.2 6.2l2 2 3.6-4" stroke="#1b1c1d" stroke-width="1.5" fill="none"/></svg><strong>Meisterschaftsspiel:</strong> Das große Finale zur Krönung<br>des Turniersiegers.</li>
  </ul>

  <div class="board-photo" role="img" aria-label="Foto einer Dartscheibe mit drei Pfeilen in Rot, Blau und Grün"></div>

  <div class="rules">
    <div class="rule"><span class="phase">Gruppenphase</span><span class="mode">301 | DO | BO3</span></div>
    <div class="rule"><span class="phase">KO-Phase</span><span class="mode">501 | DO | BO5</span></div>
  </div>

  <div class="signup">
    <span class="label">ANMELDUNG PER E-MAIL</span>
    <span class="bar"></span>
    <span class="link">besucher.tv-hallwitz.de</span>
  </div>

  <p class="website">www.<b>darts.tv-hallwitz</b>.de</p>
</main>
</body>
</html>
```